Notepads for Marketing pieces-BOLD design

Looking for notepads for marketing pieces with logo, phone number, and website. Maybe something faded in background. Looking for bold and different

```html
<!DOCTYPE html>
<html lang="en">
<head>
<meta charset="utf-8">
<title>Vitalpoint Notepad</title>
<link href="https://fonts.googleapis.com/css2?family=Poppins:wght@400;500;700&display=swap" rel="stylesheet">
<style>
  :root {
    --backdrop: #e4e4e4;
    --paper: #ffffff;
    --brand-red: #e41e26;
    --ink: #1e1b1c;
    --rule: #dccbb0;
    --footer-dark: #231f20;
  }
  * { margin: 0; padding: 0; box-sizing: border-box; }
  html, body {
    width: 1154px;
    height: 1200px;
    overflow: hidden;
    background: var(--backdrop);
    font-family: "Poppins", sans-serif;
  }
  .notepad {
    position: absolute;
    left: 153px;
    top: 0;
    width: 847px;
    height: 1200px;
    background: linear-gradient(180deg, var(--paper) 0%, #f7f7f7 100%);
  }
  .masthead {
    position: absolute;
    top: 40px;
    left: 0;
    width: 100%;
    text-align: center;
  }
  .brand-name {
    font-weight: 700;
    font-size: 50px;
    line-height: 1;
    letter-spacing: 2px;
    color: var(--brand-red);
  }
  .services {
    margin-top: 12px;
    font-weight: 500;
    font-size: 13px;
    color: var(--ink);
  }
  .services .divider { margin: 0 4px; }
  .writing-lines {
    position: absolute;
    left: 50px;
    top: 196px;
    width: 757px;
  }
  .writing-lines span {
    display: block;
    height: 36px;
    border-top: 1px solid var(--rule);
  }
  .writing-lines span:last-child { height: 0; }
  .footer-band {
    position: absolute;
    left: 0;
    bottom: 0;
    width: 847px;
    height: 52px;
  }
  .band-shape { position: absolute; left: 0; top: 0; }
  .footer-item {
    position: absolute;
    top: 0;
    height: 52px;
    display: flex;
    align-items: center;
    gap: 10px;
    color: #fff;
    font-size: 16px;
    font-weight: 400;
    line-height: 1;
    white-space: nowrap;
  }
  .footer-icon { display: block; flex-shrink: 0; }
  .footer-item.website { left: 174px; }
  .footer-item.phone { left: 636px; }
</style>
</head>
<body>
  <main class="notepad">
    <header class="masthead">
      <div class="brand-name">VITALPOINT</div>
      <div class="services">Home Health<span class="divider">|</span>Medical Staffing<span class="divider">|</span>Outpatient Therapy</div>
    </header>

    <div class="writing-lines" aria-hidden="true">
      <span></span><span></span><span></span><span></span><span></span>
      <span></span><span></span><span></span><span></span><span></span>
      <span></span><span></span><span></span><span></span><span></span>
      <span></span><span></span><span></span><span></span><span></span>
      <span></span><span></span><span></span><span></span><span></span>
    </div>

    <footer class="footer-band">
      <svg class="band-shape" width="847" height="52" viewBox="0 0 847 52" aria-hidden="true">
        <polygon points="0,0 565,0 538,52 0,52" fill="var(--brand-red)"/>
        <polygon points="577,0 847,0 847,52 551,52" fill="var(--footer-dark)"/>
      </svg>
      <div class="footer-item website">
        <svg class="footer-icon" width="16" height="16" viewBox="0 0 16 16" aria-hidden="true">
          <circle cx="8" cy="8" r="7" fill="none" stroke="#fff" stroke-width="1.6"/>
          <ellipse cx="8" cy="8" rx="3" ry="7" fill="none" stroke="#fff" stroke-width="1.2"/>
          <line x1="1" y1="8" x2="15" y2="8" stroke="#fff" stroke-width="1.2"/>
        </svg>
        <span>www.vitalpoint-care.org</span>
      </div>
      <div class="footer-item phone">
        <svg class="footer-icon" width="18" height="14" viewBox="0 0 18 14" aria-hidden="true">
          <path d="M1 5 Q9 -1 17 5 L15 7 L12 5.5 L12 3.5 Q9 2.5 6 3.5 L6 5.5 L3 7 Z" fill="var(--brand-red)"/>
          <path d="M4 8 L14 8 L15 13 L3 13 Z" fill="var(--brand-red)"/>
        </svg>
        <span>555.214.0180</span>
      </div>
    </footer>
  </main>
</body>
</html>
```